Tatami Hall Sport promotional leaflet to attract new members

We are looking to produce a leaflet for a local judo club to attract seniors and juniors 5+ the leaflet needs to encourage people to attend classes and train in the martial art

Tatami Hall Sport are proud members of the KSB UK (mats for every) and practice traditional judo which mean we wear white Gi's to show cleanliness and tradition.

www.tatamihallsport.co.uk

Target Market(s)

Kids from 5+ and Adults

Font styles to use
Serif

Requirements
Must have
• Must include times of training and how to book onto a beginners induction
• it must look enticing and show that Judo is fun for all
• must highlight we open on Tuesdays and Thursdays
• Juniors are from 6.15pm to 7.15pm
• seniors 7.30pm to 9pm
• classes are held at Vantrel Gym, Unit 7, Marlow Row, Denholm Close, Ferncombe, Hollin Vale, BN17 8QT
• We practice on a Sprung floor Mat area and is great for men and women
• first two classes free
Nice to have
• Classes are run by an expeirnced team including
• Dan Merrow 5th Dan and international referee
• Luke Merrow 2nd Dan current Global Grappling Union European Champion

```html
<!DOCTYPE html>
<html lang="en">
<head>
<meta charset="utf-8">
<title>Tatami Hall Sport – Leaflet</title>
<link href="https://fonts.googleapis.com/css2?family=Oswald:wght@700&family=Didact+Gothic&family=Quicksand:wght@500&display=swap" rel="stylesheet">
<style>
  :root {
    --red: #b3161f;
    --red-deep: #7e0d12;
    --ink: #111111;
    --paper-top: #ffffff;
    --paper-bottom: #e4e4e4;
    --photo-grey: #8a9099;
    --photo-light: #d9d9d9;
  }
  * { margin: 0; padding: 0; box-sizing: border-box; }
  html, body { width: 848px; height: 1200px; overflow: hidden; background: #ffffff; }
  .leaflet {
    position: relative; width: 848px; height: 1200px; overflow: hidden;
    background: linear-gradient(180deg, var(--paper-top) 0%, var(--paper-top) 35%, var(--paper-bottom) 100%);
    font-family: "Didact Gothic", sans-serif; color: var(--ink);
  }
  .brand { position: absolute; left: 28px; top: 34px; display: flex; align-items: center; gap: 14px; }
  .brand-dot { width: 62px; height: 62px; border-radius: 50%; background: var(--red); }
  .brand-name { font-family: "Quicksand", sans-serif; font-weight: 500; font-size: 34px; letter-spacing: 1px; color: var(--ink); }

  .open-days { position: absolute; left: 478px; top: 78px; width: 370px; font-family: "Oswald", sans-serif; font-weight: 700; text-align: center; line-height: 1; }
  .open-lead { font-size: 29px; color: var(--ink); margin-left: -16px; }
  .open-day { font-size: 70px; color: var(--red); letter-spacing: 1px; }
  .open-day.first { margin-top: 4px; margin-left: 12px; }
  .open-and { font-size: 32px; color: var(--ink); margin-left: 10px; }
  .open-day.second { margin-top: -2px; margin-left: -28px; }

  .rule-v { position: absolute; left: 796px; top: 276px; width: 2px; height: 880px; background: var(--ink); }
  .rule-h { position: absolute; left: 194px; top: 971px; width: 654px; height: 2px; background: var(--ink); }
  .rule-dot { position: absolute; width: 14px; height: 14px; border-radius: 50%; background: var(--ink); }

  .circle { position: absolute; border-radius: 50%; }
  .accent-red { left: 488px; top: 357px; width: 460px; height: 460px;
    background: radial-gradient(circle at 40% 35%, #d22a33 0%, var(--red) 45%, var(--red-deep) 100%); }
  .ring-main { left: 31px; top: 138px; width: 504px; height: 506px; background: var(--red); }
  .photo-main { left: 40px; top: 140px; width: 494px; height: 494px;
    background: linear-gradient(180deg, var(--photo-grey) 0%, #9ca2aa 50%, var(--photo-light) 80%, #c0393f 100%); }
  .ring-small { left: 258px; top: 528px; width: 352px; height: 354px; background: #3a0c0e; }
  .photo-small { left: 262px; top: 534px; width: 342px; height: 342px;
    background: linear-gradient(180deg, #8b9099 0%, #b7bbc1 45%, #e9e6df 75%, #d98a8c 100%); }

  .session { position: absolute; left: 10px; width: 250px; text-align: center; }
  .session-name { font-family: "Quicksand", sans-serif; font-weight: 500; font-size: 66px; color: var(--red); line-height: 1; letter-spacing: 2px; }
  .session-time { font-family: "Quicksand", sans-serif; font-weight: 500; font-size: 22px; color: var(--ink); margin-top: 4px; letter-spacing: 1px; }
  .juniors { top: 648px; }
  .seniors { top: 770px; }

  .venue { position: absolute; right: 72px; top: 902px; width: 620px; text-align: right; font-size: 18px; line-height: 1.15; letter-spacing: 1.1px; }

  .offer { position: absolute; left: 48px; top: 1000px; font-family: "Oswald", sans-serif; font-weight: 700; font-size: 50px; letter-spacing: 4px; color: var(--ink); line-height: 1.1; }
  .offer-free { color: var(--red); }

  .mats { position: absolute; right: 72px; top: 1086px; width: 590px; text-align: right; font-size: 18px; line-height: 1.15; letter-spacing: 1.1px; }

  .side-brand { position: absolute; left: 814px; top: 1150px; display: flex; align-items: center; gap: 6px; transform: rotate(-90deg); transform-origin: 0 0; }
  .side-dot { width: 18px; height: 18px; border-radius: 50%; background: var(--red); }
  .side-name { font-family: "Quicksand", sans-serif; font-weight: 500; font-size: 15px; letter-spacing: 1px; color: var(--ink); white-space: nowrap; }

  .footer-band { position: absolute; left: 0; top: 1156px; width: 848px; height: 44px;
    background: linear-gradient(90deg, var(--red-deep) 0%, var(--red) 50%, var(--red-deep) 100%);
    display: flex; align-items: center; justify-content: center; }
  .footer-url { font-family: "Oswald", sans-serif; font-weight: 700; font-size: 20px; color: #ffffff; letter-spacing: 0.8px; }
</style>
</head>
<body>
<main class="leaflet">
  <div class="brand">
    <span class="brand-dot"></span>
    <span class="brand-name">TATAMI HALL SPORT</span>
  </div>

  <div class="open-days">
    <div class="open-lead">We Open On</div>
    <div class="open-day first">Tuesdays<span class="open-and">And</span></div>
    <div class="open-day second">Thursdays</div>
  </div>

  <div class="rule-v"></div>
  <span class="rule-dot" style="left:790px; top:269px;"></span>
  <div class="rule-h"></div>
  <span class="rule-dot" style="left:188px; top:965px;"></span>

  <div class="circle accent-red" role="img" aria-label="Red-tinted photo of two judoka mid-throw on the mat"></div>
  <div class="circle ring-main"></div>
  <div class="circle photo-main" role="img" aria-label="Group photo of club members in white gis lined up in the training hall"></div>
  <div class="circle ring-small"></div>
  <div class="circle photo-small" role="img" aria-label="Photo of a black belt coach standing with two junior students on the mat"></div>

  <div class="session juniors">
    <div class="session-name">Juniors</div>
    <div class="session-time">6.15pm to 7.15pm</div>
  </div>
  <div class="session seniors">
    <div class="session-name">Seniors</div>
    <div class="session-time">7.30pm to 9pm</div>
  </div>

  <p class="venue">Classes Are Held At Vantrel Gym, Unit 7, Marlow Row, Denholm Close, Ferncombe, Hollin Vale, BN17 8QT</p>

  <h2 class="offer">FIRST TWO CLASSES <span class="offer-free">FREE</span></h2>

  <p class="mats">We practice on a Sprung floor Mat area and is great for men and women</p>

  <div class="side-brand">
    <span class="side-dot"></span>
    <span class="side-name">TATAMI HALL SPORT</span>
  </div>

  <footer class="footer-band">
    <span class="footer-url">www.tatamihallsport.co.uk</span>
  </footer>
</main>
</body>
</html>
```